Real Estate Broker specializing in investment property needs business card

Would like to use a tag line for my company, Larkspur Keys LLC (Right now I use Larkspur Keys - For Real Estate Needs). I you have a more creative tag line it can be used because this is a new company.
We focus on Investment Acquisition Deals; Provide Custom Marketing Strategies for Sellers; Provide Pre Listinging Value Opportunities for Buyers.
Would like a call to action, but I do not want it to look too cluttered
I would like space to be available for writing on.
I prefer vertical business cards, but it could be horizontal on one or both sides. In fact if you can create a shape other than rectangle or a cut in the rectangle that makes it memorable, relevant to real estate, yet practical...(it will be kept) that would be of value.
If you have experience with business cards please feel free to suggest the paper type, size.

Target Market(s)

Investors, Neighbors, Friends... anyone who buys or would like to sell their residence

Industry/Entity Type

Real Estate

Contact Information for Business Card

The challenge is to incorporate a logo design of the Managing Brokerage Company, Tenant's Compass, and try to brand my company, LarkspurKeys LLC. LarkspurKeys LLC could work under another managing broker but the services and contact information would remain the same.

Font styles to use
Serif

Colors

Designer to choose colors to be used in the design.

Requirements
Must have
• Real estate company named Larkspur Keys has to incorporate the logo of the managing broker company, Tenants Compass (see attached) into design of business card. (It is not a design for a logo I prefer but I need to use it. Size does not matter).
• Must also have my name, phone number and email address. (No website address yet)
• Just a few of the services we provide include
• We facilitate Investment Acquisition Deals; Provide Custom Marketing Strategies for Sellers; Provide Pre Listinging Value Opportunities for Buyers.
Nice to have
• Would like to use a tag line for my company, Larkspur Keys LLC (Right now I use Larkspur Keys - For Real Estate Needs). If you have a more creative tag line it can be used because this is a new company.
• Space to write information on, so they keep the card such as an appointment time to sit down and determine their needs
• A call to action maybe after the services? Or on the back of the card where it is blank.
• Larkspur Keys does not have a logo, If you think a logo for Tenants Compass and a logo for LarkspurKeys LLC can work, then please incorporate it into the business card.
Should not have
• Clutter
• Do not like comic style designs; prefer a sophisticated look and texture.

```html
<!DOCTYPE html>
<html lang="en">
<head>
<meta charset="utf-8">
<title>Larkspur Keys – Business Card</title>
<link rel="stylesheet" href="https://fonts.googleapis.com/css2?family=Anton&family=Great+Vibes&family=Montserrat:wght@300;400;600&display=swap">
<style>
  :root {
    --backdrop: #1e2023;
    --wine-deep: #420610;
    --wine-mid: #8a1422;
    --wine-bright: #b71f31;
    --amber: #f7b21e;
    --amber-deep: #f29a16;
    --gold: #f0b43a;
    --paper: #ffffff;
    --ink: #111111;
    --web-red: #a3142a;
  }
  * { box-sizing: border-box; margin: 0; padding: 0; }
  html, body { width: 1200px; height: 960px; overflow: hidden; background: var(--backdrop); }
  .sheet { position: relative; width: 1200px; height: 960px; }

  .card {
    position: absolute; left: 220px; width: 760px; height: 434px;
    border-radius: 28px; overflow: hidden;
    box-shadow: 0 18px 40px rgba(0,0,0,.45);
  }
  .wine {
    background:
      linear-gradient(180deg, rgba(0,0,0,.25), rgba(0,0,0,0) 40%, rgba(0,0,0,.3)),
      linear-gradient(90deg, var(--wine-deep) 0%, var(--wine-mid) 30%, var(--wine-bright) 50%, var(--wine-mid) 70%, var(--wine-deep) 100%);
  }

  /* Front */
  .card-front { top: 31px; }
  .name-band {
    position: absolute; left: 0; top: 0; width: 100%; height: 138px;
    background: linear-gradient(90deg, var(--amber-deep), var(--amber) 60%, var(--amber-deep));
    text-align: right; padding: 14px 46px 0 0; color: var(--paper);
  }
  .agent-name { font-family: "Great Vibes", cursive; font-size: 60px; line-height: 1.1; font-weight: 400; }
  .agent-role { font-family: "Montserrat", sans-serif; font-weight: 300; font-size: 22px; letter-spacing: .5px; }

  .brokerage {
    position: absolute; left: 44px; top: 226px;
    display: flex; align-items: center; gap: 14px;
  }
  .brokerage-dot { width: 26px; height: 26px; border-radius: 50%; background: var(--gold); }
  .brokerage-name { font-family: "Montserrat", sans-serif; font-weight: 600; font-size: 28px; color: var(--gold); }

  .contact-list {
    position: absolute; left: 372px; right: 40px; top: 200px; list-style: none;
    font-family: "Montserrat", sans-serif; font-weight: 300; font-size: 22px; color: var(--paper);
  }
  .contact-list li { display: flex; align-items: center; gap: 14px; height: 40px; white-space: nowrap; }
  .contact-list svg { width: 20px; height: 20px; flex: none; }

  /* Back */
  .card-back { top: 497px; background: var(--paper); }
  .services {
    position: absolute; left: 0; top: 0; width: 100%; height: 160px;
    padding: 26px 40px 0 0; text-align: right;
    font-family: "Anton", sans-serif; font-size: 27px; line-height: 1.3; color: var(--paper);
    letter-spacing: .3px;
  }
  .appointment {
    position: absolute; left: 44px; top: 188px;
    font-family: "Montserrat", sans-serif; font-weight: 600; color: var(--ink);
  }
  .appointment h2 { font-size: 22px; font-weight: 600; letter-spacing: 1px; margin-bottom: 10px; }
  .write-line { display: flex; align-items: flex-end; gap: 4px; font-size: 20px; height: 36px; }
  .write-line span.rule { display: inline-block; width: 230px; border-bottom: 2px solid var(--ink); margin-bottom: 4px; }
  .web-address {
    position: absolute; right: 44px; bottom: 34px;
    font-family: "Montserrat", sans-serif; font-weight: 600; font-size: 24px; color: var(--web-red);
  }
</style>
</head>
<body>
<main class="sheet">
  <section class="card card-front wine">
    <header class="name-band">
      <h1 class="agent-name">Larkspur Keys</h1>
      <p class="agent-role">Managing Broker</p>
    </header>
    <div class="brokerage">
      <span class="brokerage-dot"></span>
      <span class="brokerage-name">Tenant's Compass</span>
    </div>
    <ul class="contact-list">
      <li>
        <svg viewBox="0 0 20 20" aria-hidden="true"><path d="M5 2c1 0 2 3 2 4s-2 1-1 3 3 4 5 5 2-1 3-1 4 1 4 2-2 3-4 3C8 18 2 12 2 6c0-2 2-4 3-4z" fill="var(--gold)"/></svg>
        123-456-2100
      </li>
      <li>
        <svg viewBox="0 0 20 20" aria-hidden="true"><rect x="1" y="4" width="18" height="12" fill="var(--gold)"/><path d="M1 4l9 7 9-7" stroke="var(--wine-mid)" stroke-width="1.6" fill="none"/></svg>
        youremail@larkspurmail.com
      </li>
      <li>
        <svg viewBox="0 0 20 20" aria-hidden="true"><circle cx="10" cy="10" r="9" fill="var(--gold)"/><g stroke="var(--wine-mid)" stroke-width="1.3" fill="none"><ellipse cx="10" cy="10" rx="4" ry="9"/><path d="M1 10h18M3 5h14M3 15h14"/></g></svg>
        www.yourwebsite.com
      </li>
    </ul>
  </section>

  <section class="card card-back">
    <div class="services wine">
      <p>We facilitate Investment Acquisition Deals</p>
      <p>Provide Custom Marketing Strategies for Sellers</p>
      <p>Provide Pre Listinging Value Opportunities for Buyer</p>
    </div>
    <div class="appointment">
      <h2>APPOINTMENT</h2>
      <p class="write-line">DATE<span class="rule"></span></p>
      <p class="write-line">TIME<span class="rule"></span></p>
    </div>
    <p class="web-address">www.yourwebsite.com</p>
  </section>
</main>
</body>
</html>
```